New Website for Asia Travel Agency

Lantern Route Website

We want a redesign for our current website, www.lanternroute.com. We want you to get creative with our brand and present our company in a unique, creative and compelling way, that communicates our exotic destinations and tours, the local and authentic character of our travel consultants and the trustworthy and professional nature of our company.

Who is this company?

Lantern Route is an online tour operator specializing in providing tailor-made tours to eight destinations in Asia; Vietnam, Thailand, Laos, Cambodia, Indonesia, Myanmar, Japan and China. They were launched in mid February 2012 with headquarters in Bangkok, Thailand, and staffed by locals and expats with many years of experience in the travel industry, and who are committed to sharing their deep knowledge of, and passion for the region.

Local knowledge

Our consultants at Lantern Route are all locals – they know their destinations inside-out and draw upon invaluable first-hand experience and information when planning your tour. They have insights into local culture and tradition, they know the best places to visit, the most worthwhile experiences to have and, most importantly, they have the knowledge to create exactly the holiday you desire.

All hotels and activities featured in a Lantern Route tour are regularly inspected by our consultants to ensure the highest quality standards are met and that all information is correct and up to date.

Unforgettable Travel Experiences

Whether it's a cultural exploration or a beach holiday you're after – or a mix of both – Lantern Route has an itinerary for you – and if we don't have one, we'll tailor-make one! From the main sights to remote villages, our locally based Travel Specialists will give you unique insights into every place you visit and let you delve into known destinations from new perspectives.

Our tours offer a variety of hotel and resort options, premium stays in deluxe accommodation, heritage hotels, a five-star boutique or on the water in a junk. Tap into our experience let us create an experience unique to you – and one you will never forget.

What type of Holiday to Asia?

Our itineraries at Lantern Route are created according to different inspirations. Some travelers are interested in the History & Culture of a destination, while some like to stay active with Adventure tours. A Cross Border trip explores different countries in a single tour, while Ultimate Luxury tours offer the highest level of exclusivity across our destinations. There are 14 different Holiday Types to choose from, or you can mix and match ideas to create your dream vacation.

Target Market(s)

Slightly more female, aged 30-65, are creative, professional and looking for something different, something a bit unusual.

Industry/Entity Type

Boutique

Requirements
Must have
• 5 page designs:

1. Homepage
2. Tours list page for a country
3. Tour page
4. 'Be Inspired' page
5. Country page
6. Enquiry page

Our inspirations.

The following list shows websites we love and which inspire us... to give you some indication of our preferred styles, functions and layouts:

http://www.frostvale.com/en/ (we really like this, great personality, like the use of icons for tour types)
http://www.pebbletrek.co.uk/ (very simple design elements and layout)
http://www.sunmarrow.com/ (great use of background image, nice simple nav bar)
http://www.roamkestrel.org/ (we like because it has distinct personality and is well suited to the destination)
http://www.seebrantown.com/ (clear personality through font use)
http://www.vastquarry.com/ (original, unique)
http://www.ploverjournal.com/grand-tour-of-asia (like the map style)

Key design points:

1. You must use our existing logo (attached), but you can change the color scheme of the logo to accord with the whichever color scheme you choose for the main designs.
2. Our logo strapline is "Asia is our Lantern" and should be used prominently on the page to reinforce the meaning of our company name.
3. Home page and tours list pages should allow the user to see the choice of tours immediately without scrolling & Introduction copy should be minimal.
4. We and our site visitors are inspired and excited by our photography, this is an element of the site which we would like to maintain and build on, though the section page header sliders are currently too big and do not allow quick access to the section content. This is a design problem which needs a solution. Full page photographic backgrounds may be an answer?
5. Tour page should display other contextual tours, from the same country or style/type
6. We should promote press coverage in various places
7. We should display consultant profiles in various places
8. Map designs for tour page and country page, plus a modal pop out for the home page. These are complex and may have a few small photos and short descriptive text only, though this is limited by your own creativity. We will use graphics and html5/css3 so there are no creative limitations.
9. The 'Inspirations' / 'Be Inspired' page is for people who want travel and holiday ideas, who are looking for inspiration on where to go and what to do. This section needs to reflect the exotic, the unusual, the extraordinary in our destinations and tours, and we leave this to your creative genius to develop. We are also interested in how this inspirations page is related to the blog and social media content we produce daily, is there an integration here? Can we present YouTube videos, our blog posts, Facebook posts etc, on this page? This is another design challenge.
10. We would like to see designs for the tours list page which feature AJAX content filtering (for instance: http://demo.skinmorrow.com/?acn), we would like to see how to include this type of content filtering on homepage and destination page also.
11. The 'Enquiry' call to action should be on all pages and prominent.
12. The enquiry page can reflect the same fields as the existing website enquiry page

Values to be communicated:

- Exotic: Asia is exotic, and our tours will expose clients to extraordinary sights and unusual cultural encounters.
- Authentic: Our travel consultants all live in the destinations themselves, they are local nationals and have all the insider knowledge to give clients a truly authentic experience of our destinations
- Unique: All of our tours are tailor made, there are no fixed departure dates or join-in groups. All tour itineraries can be uniquely designed for our clients, from departure dates to destinations.
- Trust: Some travelers prefer to book their holidays with local agencies they can meet in person, rather than with online companies like us who live in the destinations and who they only get to meet on Skype video or phone. We want to convey that we are trustworthy. We have attempted this through presenting a 'meet the team' page and a 'press' page and advert, as well as offering a prominent international phone number. How we you build on this and further convey this value?

```html
<!DOCTYPE html>
<html lang="en">
<head>
<meta charset="utf-8">
<title>Lantern Route – Asia is our Lantern</title>
<link rel="stylesheet" href="https://fonts.googleapis.com/css2?family=Open+Sans:wght@400;600&family=PT+Sans:wght@400;700&display=swap">
<style>
:root{
  --ink:#222;
  --muted:#555;
  --accent:#1bb3d9;
  --accent-dark:#0f8fb5;
  --panel:#e4e4e4;
  --panel-edge:#d2d2d2;
  --header-bg:#f4f4f4;
  --footer-bg:#2d2d2d;
  --footer-bar:#1e1e1e;
  --footer-text:#f2f2f2;
  --tick:#2bb8de;
}
*{margin:0;padding:0;box-sizing:border-box}
html,body{width:1050px;height:1200px;overflow:hidden;background:#fff}
body{position:relative;font-family:Arial,Helvetica,sans-serif;color:var(--ink)}
.abs{position:absolute}

/* header */
.site-header{left:0;top:0;width:1050px;height:95px;background:linear-gradient(#fff,var(--header-bg));border-bottom:2px solid #e2e2e2}
.brand{left:92px;top:26px;display:flex;align-items:center;gap:10px}
.brand-mark{width:52px;height:52px;background:#cfe1e0;border:3px solid #333;border-radius:8px}
.brand-name{font-family:'PT Sans',sans-serif;font-weight:700;font-size:25px;color:#333;letter-spacing:-.5px;line-height:1}
.brand-tag{font-family:'PT Sans',sans-serif;font-weight:700;font-size:13px;color:#777;margin-top:2px;padding-left:26px}
.field{height:24px;border:1px solid #d4d4d4;background:#fff;font-family:'Open Sans',sans-serif;font-size:11px;color:#999;padding:4px 7px;letter-spacing:.5px}
.select{left:593px;top:7px;width:151px}
.select i{position:absolute;right:2px;top:3px;width:16px;height:16px;background:#555}
.select i:after{content:"";position:absolute;left:4px;top:6px;border:4px solid transparent;border-top:5px solid #fff}
.search{left:760px;top:7px;width:191px}
.search svg{position:absolute;right:3px;top:2px}
.feeds{left:743px;top:64px;font-family:'Open Sans',sans-serif;font-style:italic;font-size:12.5px;color:#555;display:flex;align-items:center;gap:10px}
.feeds span.ic{width:16px;height:16px;border-radius:3px;display:inline-block}
.feeds .ic-1{background:#f0852a;margin-left:4px}
.feeds .ic-2{background:#3b5a9a}
.feeds .ic-3{background:#4ec0e8}
.feeds .ic-4{background:#2e8a3a}

/* nav */
.main-nav{left:0;top:97px;width:1050px;height:43px;background:linear-gradient(#fff,#f1f1f1);border-bottom:1px solid #ddd}
.main-nav a{position:absolute;top:10px;font-family:'PT Sans',sans-serif;font-size:14.5px;color:#333;text-decoration:none;line-height:22px}
.main-nav a.active{background:var(--accent);color:#fff;padding:0 12px;top:9px;height:25px;line-height:25px;border-radius:2px}

/* hero */
.hero{left:0;top:140px;width:1050px;height:335px;background:linear-gradient(180deg,#3f8fd6 0%,#8cc1ea 34%,#c6e3f3 44%,#2dbccb 50%,#7dd6d4 62%,#e8d9c2 72%,#f3e9da 100%)}
.hero-wave{left:0;top:455px;width:1050px;height:22px}

/* feature cards */
.card{top:500px;width:248px;height:118px;background:var(--panel);border:1px solid var(--panel-edge);border-radius:6px}
.card-tab{top:528px;width:60px;height:60px;border-radius:50%;background:var(--panel);border:1px solid var(--panel-edge)}
.card-tab span{position:absolute;left:14px;top:19px;width:26px;height:20px;border:2px solid #444;border-radius:4px;background:#cfe1e0}
.card h2{position:absolute;left:20px;top:8px;font-family:'Open Sans',sans-serif;font-weight:400;font-size:21px;color:#444;letter-spacing:.4px}
.card .thumb{position:absolute;left:26px;top:46px;width:56px;height:56px;border:3px solid #fff;box-shadow:0 0 2px #999}
.card p{position:absolute;left:90px;top:47px;width:150px;font-size:10px;line-height:14px;color:#333}
.card p b{display:block;font-size:10px}

/* about */
.about-tab{left:89px;top:657px;width:212px;height:40px;background:#fff;border:2px solid #e6e6e6;border-bottom:none;border-radius:6px 6px 0 0;font-family:'Open Sans',sans-serif;font-size:16.5px;letter-spacing:1px;color:#222;padding:9px 0 0 15px;z-index:2}
.about-box{left:89px;top:694px;width:873px;height:212px;background:#fff;border:2px solid #e6e6e6}
.about-photo{left:103px;top:730px;width:202px;height:146px;background:#fff;border:1px solid #e2e2e2;box-shadow:0 1px 3px rgba(0,0,0,.12);padding:8px}
.about-photo div{width:100%;height:100%;background:linear-gradient(160deg,#9fb4c9 0%,#7f8f6d 30%,#6c4a3d 55%,#a98e7a 80%,#c9bfb2 100%)}
.about-text{left:327px;top:724px;width:600px;font-size:11.4px;line-height:24.5px;color:#222}
.about-text p+p{margin-top:24.5px}
.more{left:864px;top:880px;font-size:11.4px;color:#222}

/* footer */
.site-footer{left:0;top:941px;width:1050px;height:221px;background:var(--footer-bg)}
.foot-col h3{font-family:'Open Sans',sans-serif;font-weight:600;font-size:15.5px;color:var(--footer-text);margin-bottom:11px;letter-spacing:.2px}
.foot-col ul{list-style:none}
.foot-col li{font-size:11px;color:var(--footer-text);height:19.25px;padding-left:22px;position:relative}
.foot-col li svg{position:absolute;left:0;top:1px}
.divider{top:950px;width:1px;height:195px;background:#444}
.newsletter p{font-size:11px;line-height:16px;color:var(--footer-text);width:290px;margin-top:9px}
.news-input{left:664px;top:1023px;width:219px;height:33px;background:#6d6d6d;border-radius:3px 0 0 3px}
.news-btn{left:883px;top:1023px;width:41px;height:33px;background:var(--accent-dark);border-radius:0 3px 3px 0}
.foot-brand{left:670px;top:1078px;display:flex;align-items:center;gap:12px}
.foot-brand .brand-mark{width:60px;height:56px;background:#cfe1e0;border-color:#111}
.foot-brand .brand-name{color:#ddd;font-size:25px}
.foot-brand .brand-tag{color:#888}
.bottom-bar{left:0;top:1162px;width:1050px;height:38px;background:var(--footer-bar)}
.copyright{left:0;top:1170px;width:1010px;text-align:center;font-size:10px;color:#eee}
.social{left:854px;top:1169px;display:flex;gap:7px}
.social span{width:15px;height:15px;border-radius:2px;background:#3a8fd8}
</style>
</head>
<body>

<header class="abs site-header">
  <div class="abs brand">
    <span class="brand-mark"></span>
    <div>
      <div class="brand-name">Lantern Route</div>
      <div class="brand-tag">Asia is our lantern.</div>
    </div>
  </div>
  <div class="abs field select">All Categories<i></i></div>
  <div class="abs field search">Search Keywords..
    <svg width="20" height="18" viewBox="0 0 20 18"><circle cx="8" cy="7.5" r="5.5" fill="none" stroke="#666" stroke-width="2"/><path d="M12 11.5l5 5" stroke="#666" stroke-width="3" stroke-linecap="round"/></svg>
  </div>
  <div class="abs feeds">News Feeds
    <span class="ic ic-1"></span><span class="ic ic-2"></span><span class="ic ic-3"></span><span class="ic ic-4"></span>
    <svg width="18" height="14" viewBox="0 0 18 14"><rect x=".5" y=".5" width="17" height="13" fill="#f4f4f4" stroke="#aaa"/><path d="M.5 .5l8.5 7 8.5-7" fill="none" stroke="#aaa"/></svg>
  </div>
</header>

<nav class="abs main-nav">
  <a class="active" style="left:102px">Home</a>
  <a style="left:180px">Destinations</a>
  <a style="left:284px">Tours</a>
  <a style="left:354px">Holiday Types</a>
  <a style="left:466px">Best Value</a>
  <a style="left:557px">About Us</a>
  <a style="left:640px">Blog</a>
</nav>

<div class="abs hero" role="img" aria-label="Tropical beach with striped sun loungers, parasols and a boat on turquoise water"></div>
<svg class="abs hero-wave" viewBox="0 0 1050 22" preserveAspectRatio="none"><path d="M0 22V14Q525 -4 1050 10V22Z" fill="#10b4d8"/><path d="M0 22Q525 8 1050 18V22Z" fill="#fff"/></svg>

<section>
  <div class="abs card-tab" style="left:89px"><span></span></div>
  <article class="abs card" style="left:118px">
    <h2>Popular Attractions</h2>
    <div class="thumb" role="img" aria-label="Fisherman wading in shallow water" style="background:linear-gradient(160deg,#6aa3d6,#2f6fa8)"></div>
    <p><b>Fairs &amp; Festivals</b>Fairs and festivals capture the flavor of Idaho communities, with a variety occurring throughout.</p>
  </article>

  <div class="abs card-tab" style="left:387px"><span></span></div>
  <article class="abs card" style="left:416px">
    <h2>Outdoor Recreation</h2>
    <div class="thumb" role="img" aria-label="Great wall winding over green mountains" style="background:linear-gradient(180deg,#d9e2ea,#6b7f4a 60%,#3d4a26)"></div>
    <p><b>Fairs &amp; Festivals</b>Fairs and festivals capture the flavor of Idaho communities, with a variety occurring throughout.</p>
  </article>

  <div class="abs card-tab" style="left:686px"><span></span></div>
  <article class="abs card" style="left:715px">
    <h2>New Creations</h2>
    <div class="thumb" role="img" aria-label="Traditional tiled rooftops" style="background:linear-gradient(160deg,#9a8f86,#5b4d44)"></div>
    <p><b>Fairs &amp; Festivals</b>Fairs and festivals capture the flavor of Idaho communities, with a variety occurring throughout.</p>
  </article>
</section>

<section>
  <h2 class="abs about-tab">ASIA IS OUR LANTERN</h2>
  <div class="abs about-box"></div>
  <figure class="abs about-photo"><div role="img" aria-label="Red lantern hanging over a round earthen village courtyard"></div></figure>
  <div class="abs about-text">
    <p>No one knows a destination better than someone who lives, works and plays there. That's the foundation of Lantern Route. Our travel specialists reside in Asia. They live Asia, they breathe Asia. And they're intrigued explorers as much as they are citizens of Bangkok, or Bali, or Luang Prabang.</p>
    <p>The result is a travel company tailor-made for the person with a taste for veering off the well-trodden path, for the adven­turer who wants access to Asia's most spectacular sights, but hidden charms as well, on the road less traveled.</p>
  </div>
  <div class="abs more">More info [+]</div>
</section>

<footer>
  <div class="abs site-footer"></div>
  <div class="abs divider" style="left:244px"></div>
  <div class="abs divider" style="left:437px"></div>
  <div class="abs divider" style="left:632px"></div>

  <div class="abs foot-col" style="left:112px;top:958px">
    <h3>Our Lantern</h3>
    <ul>
      <li><svg width="13" height="11" viewBox="0 0 13 11"><path d="M1 6l4 4 7-9" fill="none" stroke="#2bb8de" stroke-width="2.2"/></svg>Thailand</li>
      <li><svg width="13" height="11" viewBox="0 0 13 11"><path d="M1 6l4 4 7-9" fill="none" stroke="#2bb8de" stroke-width="2.2"/></svg>Indonesia</li>
      <li><svg width="13" height="11" viewBox="0 0 13 11"><path d="M1 6l4 4 7-9" fill="none" stroke="#2bb8de" stroke-width="2.2"/></svg>Laos</li>
      <li><svg width="13" height="11" viewBox="0 0 13 11"><path d="M1 6l4 4 7-9" fill="none" stroke="#2bb8de" stroke-width="2.2"/></svg>Cambodia</li>
      <li><svg width="13" height="11" viewBox="0 0 13 11"><path d="M1 6l4 4 7-9" fill="none" stroke="#2bb8de" stroke-width="2.2"/></svg>Japan</li>
      <li><svg width="13" height="11" viewBox="0 0 13 11"><path d="M1 6l4 4 7-9" fill="none" stroke="#2bb8de" stroke-width="2.2"/></svg>Myanmar</li>
      <li><svg width="13" height="11" viewBox="0 0 13 11"><path d="M1 6l4 4 7-9" fill="none" stroke="#2bb8de" stroke-width="2.2"/></svg>Vietnam</li>
      <li><svg width="13" height="11" viewBox="0 0 13 11"><path d="M1 6l4 4 7-9" fill="none" stroke="#2bb8de" stroke-width="2.2"/></svg>China</li>
    </ul>
  </div>

  <div class="abs foot-col" style="left:266px;top:958px">
    <h3>About Lantern Route</h3>
    <ul>
      <li><svg width="13" height="11" viewBox="0 0 13 11"><path d="M1 6l4 4 7-9" fill="none" stroke="#2bb8de" stroke-width="2.2"/></svg>Why Book With Us</li>
      <li><svg width="13" height="11" viewBox="0 0 13 11"><path d="M1 6l4 4 7-9" fill="none" stroke="#2bb8de" stroke-width="2.2"/></svg>About Us</li>
      <li><svg width="13" height="11" viewBox="0 0 13 11"><path d="M1 6l4 4 7-9" fill="none" stroke="#2bb8de" stroke-width="2.2"/></svg>Meet The Team</li>
      <li><svg width="13" height="11" viewBox="0 0 13 11"><path d="M1 6l4 4 7-9" fill="none" stroke="#2bb8de" stroke-width="2.2"/></svg>Careers</li>
      <li><svg width="13" height="11" viewBox="0 0 13 11"><path d="M1 6l4 4 7-9" fill="none" stroke="#2bb8de" stroke-width="2.2"/></svg>In The Press</li>
      <li><svg width="13" height="11" viewBox="0 0 13 11"><path d="M1 6l4 4 7-9" fill="none" stroke="#2bb8de" stroke-width="2.2"/></svg>Affiliate Program</li>
    </ul>
  </div>

  <div class="abs foot-col" style="left:463px;top:962px">
    <h3>Quick Links</h3>
    <ul>
      <li><svg width="13" height="11" viewBox="0 0 13 11"><path d="M1 6l4 4 7-9" fill="none" stroke="#2bb8de" stroke-width="2.2"/></svg>Home</li>
      <li><svg width="13" height="11" viewBox="0 0 13 11"><path d="M1 6l4 4 7-9" fill="none" stroke="#2bb8de" stroke-width="2.2"/></svg>Destinations</li>
      <li><svg width="13" height="11" viewBox="0 0 13 11"><path d="M1 6l4 4 7-9" fill="none" stroke="#2bb8de" stroke-width="2.2"/></svg>Tours</li>
      <li><svg width="13" height="11" viewBox="0 0 13 11"><path d="M1 6l4 4 7-9" fill="none" stroke="#2bb8de" stroke-width="2.2"/></svg>Holiday Types</li>
      <li><svg width="13" height="11" viewBox="0 0 13 11"><path d="M1 6l4 4 7-9" fill="none" stroke="#2bb8de" stroke-width="2.2"/></svg>Best Value</li>
      <li><svg width="13" height="11" viewBox="0 0 13 11"><path d="M1 6l4 4 7-9" fill="none" stroke="#2bb8de" stroke-width="2.2"/></svg>About Us</li>
      <li><svg width="13" height="11" viewBox="0 0 13 11"><path d="M1 6l4 4 7-9" fill="none" stroke="#2bb8de" stroke-width="2.2"/></svg>Blog</li>
    </ul>
  </div>

  <div class="abs foot-col newsletter" style="left:662px;top:952px">
    <h3>Join Our Newsletter</h3>
    <p>Stay up to date with all our latest tips to improve your websites performance with our newsletter.</p>
  </div>
  <div class="abs news-input"></div>
  <div class="abs news-btn">
    <svg width="41" height="33" viewBox="0 0 41 33"><circle cx="17" cy="16" r="7" fill="none" stroke="#fff" stroke-width="1.6"/><path d="M10 16h14M17 9v14" stroke="#fff" stroke-width="1.2"/><circle cx="23" cy="15" r="4.5" fill="#0f8fb5" stroke="#fff" stroke-width="1.8"/><path d="M26 18l5 5" stroke="#fff" stroke-width="2.5" stroke-linecap="round"/></svg>
  </div>
  <div class="abs foot-brand">
    <span class="brand-mark"></span>
    <div>
      <div class="brand-name">Lantern Route</div>
      <div class="brand-tag">Asia is our lantern.</div>
    </div>
  </div>

  <div class="abs bottom-bar"></div>
  <div class="abs copyright">Copyright © 2013 Lantern Route, LLC. All rights reserved.</div>
  <div class="abs social"><span></span><span></span><span></span><span></span><span></span></div>
</footer>

</body>
</html>
```